Business Card Design

Our Motto is "Protecting Australia's Underground Utilities"

We want the Southern Cross inside a shield I have attached the southern cross and our old shield design

Product description is: Vacuum Excavation & Utility Location
Wet & Dry Vacuum Loading
Confined Space Entry Specialists
High Pressure Cleaning

The Southern Cross in the shield must be blue and white. The Company name must be Coastal Pipeline Guard. The Green & Gold Shield logo I uploaded is my OLD logo design. Thank you

Target Market(s)

Civil Construction

Industry/Entity Type

Business

Contact Information for Business Card

Coastal Pipeline Guard Pty Ltd
Corey Hallworth(Director)
0413862051
coreyh@pipeguardco.com.au
A.B.N.52938407716

Colors
0456a3

Requirements
Must have
• Southern Cross inside a shield, Blue and white design on the Southern Cross shield.
Must say Coastal Pipeline Guard P/L

```html
<!DOCTYPE html>
<html lang="en">
<head>
<meta charset="utf-8">
<title>Coastal Pipeline Guard – Business Card</title>
<link rel="stylesheet" href="https://fonts.googleapis.com/css2?family=Open+Sans:wght@400;600;700&display=swap">
<style>
  :root {
    --canvas-bg: #d5d5d7;
    --navy: #2d2a7b;
    --map-blue: 43, 42, 130;
    --night-top: #0b0b10;
    --night-bottom: #16161d;
    --card-white: #ffffff;
    --ink: #111111;
    --white: #ffffff;
  }
  * { box-sizing: border-box; margin: 0; padding: 0; }
  html, body {
    width: 883px; height: 1200px; overflow: hidden;
    background: var(--canvas-bg);
    font-family: "Open Sans", Arial, sans-serif;
  }
  .card {
    position: absolute; left: 268px; width: 390px; height: 220px;
    overflow: hidden; box-shadow: 0 3px 8px rgba(0,0,0,.18);
  }
  .card--front { top: 687px; }
  .card--back { top: 922px; height: 219px; background: var(--card-white); }

  .night-sky {
    position: absolute; inset: 0;
    background: radial-gradient(circle at 40% 35%, #1d1d26 0%, var(--night-top) 60%, var(--night-bottom) 100%);
  }
  .map-area {
    position: absolute; left: 236px; top: 14px; width: 136px; height: 198px;
    background: radial-gradient(ellipse at 50% 50%,
      rgba(var(--map-blue), 1) 0%,
      rgba(var(--map-blue), .85) 45%,
      rgba(var(--map-blue), 0) 72%);
  }
  .brand-mark {
    position: absolute; width: 68px; height: 68px; border-radius: 50%;
    background: var(--navy);
  }
  .card--front .brand-mark { left: 164px; top: 44px; background: #3a3790; }
  .card--back .brand-mark { left: 237px; top: 70px; }

  .brand-name {
    position: absolute; text-align: center; font-weight: 700; line-height: 1.15;
  }
  .card--front .brand-name { left: 60px; width: 282px; top: 128px; color: var(--white); font-size: 16px; }
  .card--back .brand-name { left: 140px; width: 260px; top: 150px; color: var(--ink); font-size: 16.5px; }
  .brand-name small { display: block; font-size: 11px; font-weight: 700; }

  .name-band {
    position: absolute; left: 0; top: 22px; width: 162px; height: 38px;
    background: var(--navy); color: var(--white); padding: 4px 0 0 25px;
  }
  .name-band .person { font-size: 14px; line-height: 17px; font-weight: 400; }
  .name-band .role { font-size: 9px; line-height: 11px; }

  .address {
    position: absolute; left: 25px; top: 89px; font-size: 10.5px; line-height: 14px; color: var(--ink);
  }
  .contacts {
    position: absolute; left: 24px; top: 139px; list-style: none;
    font-size: 10.5px; line-height: 11.5px; color: var(--ink);
  }
  .contacts li { display: flex; align-items: center; gap: 10px; }
  .contacts svg { width: 9px; height: 9px; flex: none; }
  .contacts .fx { width: 9px; font-size: 7px; color: var(--navy); font-weight: 700; }
</style>
</head>
<body>
  <section class="card card--front" aria-label="Business card front">
    <div class="night-sky" role="img" aria-label="Starry night sky photograph"></div>
    <div class="map-area" role="img" aria-label="Map of Australia in blue"></div>
    <div class="brand-mark"></div>
    <p class="brand-name">Coastal Pipeline Guard<small>Pty Ltd</small></p>
  </section>

  <section class="card card--back" aria-label="Business card back">
    <div class="name-band">
      <p class="person">Corey Hallworth</p>
      <p class="role">Director</p>
    </div>
    <p class="address">Your address can put here<br>Your address can put here</p>
    <ul class="contacts">
      <li><svg viewBox="0 0 10 10"><path d="M1 4 Q5 0 9 4 L8 5 L6 4 V3 H4 V4 L2 5 Z M2 6 H8 V9 H2 Z" fill="#2d2a7b"/></svg>0123 456 789</li>
      <li><svg viewBox="0 0 10 10"><rect x="2" y="0.5" width="6" height="9" rx="1" fill="#2d2a7b"/><rect x="3" y="1.8" width="4" height="5" fill="#fff"/><circle cx="5" cy="8.2" r=".6" fill="#fff"/></svg>0123 456 789</li>
      <li><span class="fx">Fx</span>0123 456 789</li>
      <li><svg viewBox="0 0 10 10"><rect x="0.5" y="2" width="9" height="6" fill="#2d2a7b"/><path d="M0.5 2 L5 5.5 L9.5 2" fill="none" stroke="#fff" stroke-width=".8"/></svg>youremail@mail.com</li>
    </ul>
    <div class="brand-mark"></div>
    <p class="brand-name">Coastal Pipeline Guard<small>Pty Ltd</small></p>
  </section>
</body>
</html>
```